Business Card Design for Cybersecurity Company - Quorvent Systems

We need a business card design for our new cybersecurity company, Quorvent. We’re going for a clean, hi tech look that feels modern, premium, and trustworthy. We want a design that really stands out and makes people say WOW when we hand it over!

Quorvent delivers reliable IT support and managed services for small and mid sized businesses. We help companies stay secure, efficient, and connected through proactive monitoring, cybersecurity services, cloud management, and remote support.

Target Market(s)

Designers should target small and mid sized businesses that need dependable cybersecurity and IT support.

Industry/Entity Type

Cybersecurity, Managed Service Provider, IT services

Contact Information for Business Card

Contact information

Requirements
Must have
• The card should look clean, modern, and tech focused, with the Quorvent logo, clear contact info, and strong readability. It needs to feel premium and professional while still keeping a simple layout that fits a cybersecurity and IT brand.
Nice to have
• Nice to have elements include subtle touches that give the card a modern, tech feel, along with a layout that works well in different background styles.
Should not have
• The card should avoid clutter, loud graphics, or anything that takes attention away from the logo and contact details.

```html
<!DOCTYPE html>
<html lang="en">
<head>
<meta charset="utf-8">
<title>Quorvent Systems – Business Card</title>
<link rel="stylesheet" href="https://fonts.googleapis.com/css2?family=Montserrat:wght@400;500;600&display=swap">
<style>
  :root {
    --backdrop: #a2a3a3;
    --card-front: #ffffff;
    --card-back: #6f4a9b;
    --brand: #6a4a9e;
    --ink-light: #ffffff;
    --ink-soft: #bba8d8;
    --rule: rgba(255, 255, 255, 0.55);
  }
  * { margin: 0; padding: 0; box-sizing: border-box; }
  html, body {
    width: 1200px; height: 1200px; overflow: hidden;
    background: var(--backdrop);
    font-family: "Montserrat", Arial, sans-serif;
  }
  .canvas { position: relative; width: 1200px; height: 1200px; }
  .card {
    position: absolute; left: 179px; width: 861px; height: 496px;
  }
  .card--front { top: 84px; background: var(--card-front); }
  .card--back { top: 622px; background: var(--card-back); color: var(--ink-light); }

  .brand-lockup {
    position: absolute; left: 0; right: 0; top: 248px;
    transform: translateY(-50%);
    display: flex; align-items: center; justify-content: center; gap: 18px;
  }
  .brand-lockup__dot {
    width: 40px; height: 40px; border-radius: 50%; background: var(--brand);
  }
  .brand-lockup__name {
    font-weight: 600; font-size: 58px; color: var(--brand); letter-spacing: 0.5px;
  }

  .identity {
    position: absolute; right: 473px; top: 199px; text-align: right;
    white-space: nowrap;
  }
  .identity__name { font-weight: 600; font-size: 32px; line-height: 38px; }
  .identity__role { font-weight: 400; font-size: 21px; line-height: 26px; color: var(--ink-soft); margin-top: 8px; }

  .divider {
    position: absolute; left: 411px; top: 173px; width: 1px; height: 149px;
    background: var(--rule);
  }

  .contacts {
    position: absolute; left: 425px; top: 172px; list-style: none;
    font-size: 23px; line-height: 37.5px; letter-spacing: 0.4px;
    white-space: nowrap;
  }
  .contacts__label { font-weight: 600; margin-right: 6px; }

  .footer-name {
    position: absolute; left: 0; right: 0; top: 403px; text-align: center;
    font-size: 21px; color: var(--ink-soft);
  }
</style>
</head>
<body>
<main class="canvas">
  <section class="card card--front">
    <div class="brand-lockup">
      <span class="brand-lockup__dot"></span>
      <span class="brand-lockup__name">Quorvent</span>
    </div>
  </section>

  <section class="card card--back">
    <div class="identity">
      <p class="identity__name">Owen Marsh</p>
      <p class="identity__role">Owner | CEO</p>
    </div>
    <div class="divider"></div>
    <ul class="contacts">
      <li><span class="contacts__label">P:</span>(855) 340-QRVT</li>
      <li><span class="contacts__label">M:</span>(555) 014-2286</li>
      <li><span class="contacts__label">E:</span>owen@quorvent.com</li>
      <li><span class="contacts__label">W:</span>quorvent.com</li>
    </ul>
    <p class="footer-name">Quorvent Systems</p>
  </section>
</main>
</body>
</html>
```